body balm label design

body balm tube design, current label design for other similar products
Need to have a design which can interchange between 3 different solutions
Amber Tide (Lavender + Vanilla)
Copper Harbor (Eucalyptus + Mint)
Velvet Arc (Bergamot + Cedarwood)
Tube size:
2.5h x 3.25 w
Target Market(s)
natural, solution focused
Requirements
Must have
- relatable to existing brand designs, focus on features and benefits

```html
<!DOCTYPE html>
<html lang="en">
<head>
<meta charset="utf-8">
<title>Copper Harbor Natural Body Balm Label</title>
<link rel="stylesheet" href="https://fonts.googleapis.com/css2?family=Montserrat:wght@300;600&family=Playfair+Display:wght@400&family=Parisienne&family=Libre+Baskerville&display=swap">
<style>
  :root {
    --leaf: #74a461;
    --leaf-pale: #cfe0c6;
    --paper: #ffffff;
  }
  html, body { margin: 0; padding: 0; overflow: hidden; background: var(--paper); }
  .label {
    position: relative; width: 1200px; height: 923px; overflow: hidden;
    background: var(--paper); color: var(--leaf);
    font-family: "Montserrat", sans-serif; font-weight: 300;
  }
  .rotated {
    position: absolute; white-space: nowrap;
    transform: translate(-50%, -50%) rotate(-90deg);
  }
  .botanical {
    position: absolute; left: 150px; top: 40px; width: 420px; height: 860px;
    background: radial-gradient(ellipse at 50% 45%, rgba(207,224,198,0.55), rgba(207,224,198,0.15) 60%, rgba(255,255,255,0) 75%);
  }
  .product-name {
    left: 392px; top: 402px;
    font-family: "Playfair Display", serif; font-size: 122px; letter-spacing: 0.2em;
    line-height: 1;
  }
  .product-sub {
    left: 478px; top: 160px;
    font-family: "Parisienne", cursive; font-size: 62px; line-height: 1;
  }
  .divider {
    position: absolute; left: 490px; top: 270px; width: 4px; height: 653px;
    background: var(--leaf);
  }
  .arch {
    position: absolute; left: 537px; top: 60px; width: 187px; height: 863px;
    background: var(--leaf); border-radius: 94px 94px 0 0;
  }
  .brand-mark {
    position: absolute; left: 537px; top: 115px; width: 187px; text-align: center;
    color: var(--paper); font-size: 15px; font-weight: 300; letter-spacing: 0.2em;
  }
  .brand-mark .dot {
    display: block; width: 10px; height: 10px; margin: 0 auto 8px;
    border-radius: 50%; background: var(--paper);
  }
  .balm-title {
    left: 632px; top: 525px; color: var(--paper);
    font-size: 52px; line-height: 64px; letter-spacing: 0.02em; text-align: left;
  }
  .scent {
    left: 800px; top: 395px;
    font-family: "Parisienne", cursive; font-size: 92px; line-height: 1;
  }
  .scent .plus { font-family: "Montserrat", sans-serif; font-size: 30px; vertical-align: middle; margin: 0 18px; }
  .details { position: absolute; left: 956px; top: 150px; width: 220px; }
  .details h2 {
    margin: 0 0 6px; font-size: 17px; font-weight: 600; letter-spacing: 0.08em;
  }
  .details p {
    margin: 0 0 20px; font-size: 17px; line-height: 24.5px; letter-spacing: 0.08em;
  }
  .social { position: absolute; left: 957px; top: 747px; display: flex; gap: 15px; }
  .social span { width: 40px; height: 40px; border-radius: 50%; background: var(--leaf); }
  .maker {
    position: absolute; left: 908px; top: 808px; font-size: 18px; letter-spacing: 0.08em;
  }
  .site {
    position: absolute; left: 914px; top: 839px; font-size: 15px; font-weight: 600; letter-spacing: 0.12em;
  }
  .weight {
    position: absolute; left: 88px; top: 818px; font-size: 28px; line-height: 38px; letter-spacing: 0.02em;
  }
  .origin-seal { position: absolute; left: 70px; top: 600px; }
  .origin-seal text { fill: var(--leaf); font-family: "Libre Baskerville", serif; }
</style>
</head>
<body>
<main class="label">
  <div class="botanical" role="img" aria-label="Line illustration of eucalyptus branches and leaves"></div>

  <div class="rotated product-name">HARBOR</div>
  <div class="rotated product-sub">copper</div>
  <div class="divider"></div>

  <div class="arch"></div>
  <div class="brand-mark"><span class="dot"></span>VERDANT LOOM</div>
  <div class="rotated balm-title">NATURAL<br>BODY BALM</div>

  <div class="rotated scent">Eucalyptus<span class="plus">+</span>Mint</div>

  <section class="details">
    <h2>Ingredients:</h2>
    <p>Shea butter, cocoa butter, coconut oil, sweet almond oil, beeswax, lavender essential oil, vanilla extract or vanilla oleoresin, vitamin E oil</p>
    <h2>How to use:</h2>
    <p>Gently push the balm up from the bottom of the tube using your finger, apply it directly to your skin.</p>
  </section>

  <div class="social" aria-label="Social links"><span></span><span></span><span></span></div>
  <div class="maker">Made by Verdant Loom</div>
  <div class="site">WWW.VERDANTLOOM.CA</div>

  <div class="weight">NET WT 4 oz<br>/120g</div>

  <svg class="origin-seal" width="150" height="160" viewBox="0 0 150 160" aria-label="Made in Canada, 100% natural">
    <defs>
      <path id="seal-arc" d="M 62 140 A 62 62 0 0 1 140 30"/>
    </defs>
    <text font-size="21"><textPath href="#seal-arc">Made In Canada</textPath></text>
    <text x="58" y="72" font-size="22">100%</text>
    <text x="57" y="96" font-size="12">NATURAL</text>
  </svg>
</main>
</body>
</html>
```